New Website for ReBranded Company - CrewBeacon

We have a successful company and website currently but it is a little dated. We have re-branded the company from Harbor Signal Networks to CrewBeacon and have a new logo for the new name. We are looking to build a newer fresher website with the new name. I will need a concept of the home page and one inside page. You can see our current site at https://www.harborsignalnetworks.example and the new site will be https://www.crewbeacon.example .

I also really like the https://www.pathmolder.example/ website. I like ledgerleaf.example website. I like the https://skillbinder.example/ website.

See the attached document for layout and some text to use. Use the pictures I attached as opposed to pictures from the old site as much as you can.

Target Market(s)

Business

Industry/Entity Type

Software Service

Number of Pages Required

2 page

Font styles to use
Sans Serif

Requirements
Must have
• Use the colors from my logo. Professional but modern. We want people to feel like our product makes their staff feel safer at work.
Should not have
• Don't use any red or orange (no stop colors).

```html
<!DOCTYPE html>
<html lang="en">
<head>
<meta charset="utf-8">
<title>CrewBeacon – Feel confident that your staff is protected</title>
<link rel="stylesheet" href="https://fonts.googleapis.com/css2?family=Montserrat:wght@400;500;600;700;800&display=swap">
<style>
:root{
  --blue:#3a8fd6;
  --blue-deep:#2a74b8;
  --green:#6cb33f;
  --navy:#12283a;
  --ink:#1d1f22;
  --muted:#5b6570;
  --paper:#ffffff;
  --mist:#f3f5f8;
  --ring:#e9eff5;
  --line:#d8e4ef;
}
*{box-sizing:border-box;margin:0;padding:0}
html,body{width:1200px;height:4256px;overflow:hidden}
body{position:relative;font-family:'Montserrat',sans-serif;color:var(--ink);background:var(--paper)}
.abs{position:absolute}
.btn{position:absolute;display:flex;align-items:center;justify-content:center;color:#fff;font-weight:600;font-size:14px;letter-spacing:.5px;text-transform:uppercase;border-radius:2px}
.btn.green{background:var(--green)}
.btn.blue{background:var(--blue)}
.hl{color:var(--blue)}
.hl-green{color:var(--green)}

/* hero */
.hero{position:absolute;left:0;top:0;width:1200px;height:562px;overflow:hidden}
.hero-photo{position:absolute;inset:0;background:linear-gradient(100deg,#203652 0%,#2d4868 40%,#1b2b3d 70%,#31465c 100%)}
.brand{position:absolute;display:flex;align-items:center;gap:10px;font-weight:600;color:var(--blue)}
.brand .dot{width:44px;height:44px;border-radius:50%;background:var(--blue)}
.nav{position:absolute;top:36px;left:610px;display:flex;align-items:center;height:30px;gap:32px;font-size:11.5px;font-weight:700;color:#fff}
.nav .active{color:var(--blue)}
.nav .cta{background:var(--blue);padding:0 14px;height:30px;display:flex;align-items:center;border-radius:2px;margin-left:0}
.play{position:absolute;left:172px;top:202px;width:112px;height:112px;border-radius:50%;border:1.5px solid rgba(255,255,255,.5);display:flex;align-items:center;justify-content:center}
.play span{width:70px;height:70px;border-radius:50%;background:var(--blue);display:flex;align-items:center;justify-content:center}
.watch{left:128px;top:332px;color:#fff;font-weight:700;font-size:18px}
.hero-title{left:643px;top:160px;color:#fff;font-weight:800;font-size:44px;line-height:46px;text-transform:uppercase;letter-spacing:.5px}
.hero-sub{left:643px;top:324px;color:var(--green);font-weight:700;font-size:16px}

/* feature card */
.lead-band{position:absolute;left:0;top:562px;width:1200px;height:785px;background:var(--mist)}
.features{position:absolute;left:74px;top:516px;width:1050px;height:286px;background:#fff;border:1px solid #e3e7eb;box-shadow:0 3px 10px rgba(0,0,0,.06)}
.feature{position:absolute;top:24px;width:308px}
.feature .photo{height:149px}
.feature .copy{display:flex;gap:10px;margin-top:20px;font-size:16px;font-weight:500;line-height:22px}
.feature svg{flex:none}

.alone-title{left:60px;width:466px;top:918px;text-align:center;font-weight:800;font-size:21px;line-height:26px;text-transform:uppercase}
.alone-text{left:60px;width:466px;top:1014px;text-align:center;font-size:17px;line-height:22px;font-weight:500}
.mockup{position:absolute;border-radius:10px;background:linear-gradient(160deg,#f4f7fa,#dfe6ed)}

/* why */
.why{position:absolute;left:0;top:1347px;width:1200px;height:570px;overflow:hidden;background:#fff}
.section-title{position:absolute;left:0;width:1200px;text-align:center;font-weight:800;font-size:21px;text-transform:uppercase}
.why-item{position:absolute;text-align:center;font-size:13px;line-height:17px;color:var(--muted)}
.why-item h3{font-size:15px;font-weight:700;color:var(--ink);margin-bottom:4px}
.inner-name{position:absolute;left:432px;top:505px;width:336px;text-align:center;font-size:34px;font-weight:700;color:var(--blue)}

/* stats */
.stats{position:absolute;left:0;top:1917px;width:1200px;height:703px;background:linear-gradient(160deg,#3b8fd4 0%,#2f7fc4 55%,#3a8ed2 100%);color:#fff}
.stats-lead{top:90px;left:0;width:1200px;text-align:center;font-size:17px;font-weight:500}
.stats-title{top:132px;left:0;width:1200px;text-align:center;font-size:21px;line-height:27px;font-weight:800;text-transform:uppercase}
.map{position:absolute;left:264px;top:232px;width:670px;height:330px;border-radius:8px;background:radial-gradient(ellipse at center,rgba(255,255,255,.22),rgba(255,255,255,.04) 70%)}
.big-num{font-weight:300;font-size:190px;line-height:1}
.num-label{font-size:15px;font-weight:500;text-align:center}

/* plan */
.plan{position:absolute;left:0;top:2620px;width:1200px;height:645px;background:#fff}
.underline{position:absolute;left:560px;top:114px;width:80px;height:4px;background:var(--green)}
.step{position:absolute;width:248px;height:248px;border-radius:50%;background:var(--ring);text-align:center}
.step .num{margin-top:100px;color:var(--green);font-weight:600;font-size:16px}
.step h4{margin-top:22px;font-size:16px;font-weight:700;line-height:20px}
.step p{margin-top:14px;font-size:14px;line-height:17px;color:var(--muted)}
.step-icon{position:absolute;left:104px;top:-10px}

/* connected */
.connected{position:absolute;left:0;top:3265px;width:1200px;height:595px;background:var(--mist)}
.connected-title{left:750px;top:160px;font-weight:800;font-size:21px;line-height:25px;text-transform:uppercase}

/* footer */
.footer{position:absolute;left:0;top:3860px;width:1200px;height:396px;background:var(--navy);color:#fff}
.newsletter{position:absolute;left:74px;top:3810px;width:1050px;height:99px;background:#fff;border:1px solid #e3e7eb;box-shadow:0 3px 10px rgba(0,0,0,.08)}
.newsletter h2{position:absolute;left:46px;top:36px;font-weight:800;font-size:21px;text-transform:uppercase}
.newsletter .field{position:absolute;left:503px;top:27px;width:344px;height:46px;background:#f1f3f5;color:#8a929a;font-size:14px;display:flex;align-items:center;padding-left:20px}
.newsletter .btn{left:847px;top:27px;width:158px;height:46px}
.foot-about{left:83px;top:182px;width:230px;font-size:11px;line-height:15px;font-weight:500}
.foot-col{position:absolute;top:109px;font-size:11px}
.foot-col h5{font-size:11px;font-weight:700;letter-spacing:.5px;padding-bottom:8px;border-bottom:1px solid rgba(255,255,255,.5);width:78px;margin-bottom:14px}
.foot-col li{list-style:none;line-height:15.5px;font-weight:500}
.call{position:absolute;left:912px;top:100px;width:205px;height:91px;border:2px solid var(--green);display:flex;align-items:center;gap:14px;padding-left:14px}
.call b{display:block;font-size:11px}
.call strong{font-size:17px}
.social{position:absolute;left:85px;top:310px;display:flex;gap:16px}
.social span{width:12px;height:12px;border-radius:50%;background:#fff}
.legal-links{right:83px;top:312px;font-size:10px;font-weight:600;text-align:right;line-height:18px}
</style>
</head>
<body>

<header class="hero">
  <div class="hero-photo" role="img" aria-label="Photo of a hand reaching into a jeans pocket for a wearable panic button"></div>
  <div class="brand" style="left:74px;top:28px;font-size:30px"><span class="dot"></span>CrewBeacon</div>
  <nav class="nav">
    <span class="active">HOME</span><span>BUY ADDONS</span><span>CUSTOMER LOGIN</span><span class="cta">EXPLORE YOUR CHOICES</span>
  </nav>
  <div class="play"><span><svg width="24" height="26" viewBox="0 0 24 26"><path d="M3 2l19 11L3 24z" fill="#fff"/></svg></span></div>
  <div class="abs watch">Watch How It Works</div>
  <h1 class="abs hero-title">Feel confident<br>that your staff<br>is protected</h1>
  <p class="abs hero-sub">Get a revolutionary new electronic panic button</p>
  <svg class="abs" style="left:556px;top:318px" width="78" height="36" viewBox="0 0 78 36"><path d="M76 24C50 34 24 30 6 14" fill="none" stroke="var(--green)" stroke-width="2.5"/><path d="M4 26L4 10 18 14" fill="none" stroke="var(--green)" stroke-width="2.5"/></svg>
  <div class="btn green" style="left:641px;top:367px;width:239px;height:36px;font-size:15px">Ready to get started</div>
</header>

<div class="lead-band"></div>

<section class="features">
  <div class="feature" style="left:37px">
    <div class="photo" role="img" aria-label="Photo of a hand pressing a panic button mounted under a desk" style="background:linear-gradient(150deg,#8a949c,#3f4a52)"></div>
    <div class="copy"><svg width="46" height="46" viewBox="0 0 46 46"><path d="M8 14a20 20 0 0 1 30 0M13 19a13 13 0 0 1 20 0" fill="none" stroke="var(--green)" stroke-width="2.5"/><circle cx="23" cy="28" r="4" fill="var(--blue)"/><path d="M23 32v10" stroke="var(--blue)" stroke-width="2.5"/></svg>Problems stopped before they start for any type of organization.</div>
  </div>
  <div class="feature" style="left:371px">
    <div class="photo" role="img" aria-label="Photo of several panic button devices on a table" style="background:linear-gradient(150deg,#f0e4d3,#c9b79f)"></div>
    <div class="copy"><svg width="28" height="46" viewBox="0 0 28 46"><path d="M14 2l10 10v30H4V12z" fill="none" stroke="var(--blue)" stroke-width="2"/><text x="14" y="34" font-size="15" font-family="Montserrat,sans-serif" fill="var(--green)" text-anchor="middle" font-weight="700">$</text></svg>Affordable prices starting at $18 per month. No contracts. No hidden costs.</div>
  </div>
  <div class="feature" style="left:705px">
    <div class="photo" role="img" aria-label="Photo of an office desk phone beside a panic button" style="background:linear-gradient(150deg,#c9d3d9,#5c6a73)"></div>
    <div class="copy"><svg width="40" height="46" viewBox="0 0 40 46"><path d="M20 3l15 6v12c0 11-7 18-15 22C12 39 5 32 5 21V9z" fill="none" stroke="var(--green)" stroke-width="2.5"/><path d="M20 13v14" stroke="var(--blue)" stroke-width="3"/><circle cx="20" cy="33" r="2" fill="var(--blue)"/></svg>Alerts by computer, mobile device, text, phone, email, monitoring and E911.</div>
  </div>
</section>

<h2 class="abs alone-title">Your employees shouldn't feel<br>alone <span class="hl">when they need help</span></h2>
<p class="abs alone-text">Does this problem make you feel frustrated and anxious? Put a simple solution in their hands</p>
<div class="btn blue" style="left:183px;top:1081px;width:219px;height:36px">Ready to get started</div>
<div class="mockup" style="left:520px;top:884px;width:620px;height:389px" role="img" aria-label="Laptop and phone showing the alert dashboard, with a panic button device in front"></div>

<section class="why">
  <h2 class="section-title" style="top:80px">Why businesses <span class="hl">choose us</span></h2>
  <div class="why-item" style="left:440px;top:152px;width:320px"><h3>Communicate the Way You Want</h3>We give you lots of options:<br>Computer, Mobile, Email, Phone call,<br>Text, E911, Call Center</div>
  <svg class="abs" style="left:0;top:0" width="1200" height="570" viewBox="0 0 1200 570">
    <circle cx="600" cy="515" r="228" fill="none" stroke="var(--green)" stroke-width="2"/>
    <circle cx="600" cy="515" r="168" fill="#f1f4f7"/>
    <circle cx="600" cy="286" r="41" fill="var(--green)"/>
    <path d="M584 276h22v14h-14l-8 6z M596 282h14v12l4 4-9-3h-9" fill="none" stroke="#fff" stroke-width="2"/>
    <circle cx="397" cy="413" r="41" fill="var(--blue)"/>
    <path d="M393 426v-22a4 4 0 0 1 8 0v12l9 2v10l-4 6h-11l-6-9z" fill="none" stroke="#fff" stroke-width="2"/>
    <circle cx="802" cy="413" r="41" fill="var(--blue)"/>
    <path d="M802 395l14 5v10c0 9-6 15-14 18-8-3-14-9-14-18v-10z" fill="none" stroke="#fff" stroke-width="2"/>
    <path d="M795 412l5 5 9-9" fill="none" stroke="#fff" stroke-width="2.5"/>
  </svg>
  <div class="inner-name">CrewBeacon</div>
  <div class="why-item" style="left:58px;top:370px;width:280px"><h3>Easy to Use</h3>Press a button and let the right people know you need help and open a chat window letting everyone talk on resolving their problem.</div>
  <div class="why-item" style="left:855px;top:374px;width:270px"><h3>Cost Effective Protection</h3>By leveraging your existing network and equipment we can lower your costs to give better options to your staff.</div>
</section>

<section class="stats">
  <p class="abs stats-lead">We know how scary it can feel to worry about employee safety.</p>
  <h2 class="abs stats-title">That's why we have provided a way for customers<br>to get help to staff effectively in</h2>
  <div class="map" role="img" aria-label="Dotted world map with location markers"></div>
  <div class="abs" style="left:36px;top:300px;width:250px;text-align:center"><div class="big-num">45</div><div class="num-label" style="margin-top:22px">States in USA</div></div>
  <div class="abs" style="left:1030px;top:300px;width:145px;text-align:center"><div class="big-num">5</div><div class="num-label" style="margin-top:12px;line-height:17px">Countries around<br>the globe</div></div>
  <div class="btn green" style="left:491px;top:594px;width:218px;height:36px">Start my demo</div>
</section>

<section class="plan">
  <h2 class="section-title" style="top:78px">Simple <span class="hl">start plan</span></h2>
  <div class="underline"></div>
  <svg class="abs" style="left:0;top:0" width="1200" height="645" viewBox="0 0 1200 645">
    <g fill="none" stroke="#9cc4e6" stroke-width="1.5" stroke-dasharray="5 5">
      <path d="M91 318A170 170 0 0 1 431 318"/>
      <path d="M430 306A170 170 0 0 0 770 306"/>
      <path d="M767 318A170 170 0 0 1 1107 318"/>
    </g>
    <path d="M423 330h18l-9 10z" fill="#8fa0ad"/>
    <path d="M759 310h18l-9-10z" fill="#8fa0ad"/>
  </svg>
  <div class="step" style="left:137px;top:182px">
    <svg class="step-icon" width="44" height="44" viewBox="0 0 44 44"><g fill="none" stroke="var(--blue)" stroke-width="2.5"><path d="M6 2v40M6 10h30M6 22h30M6 34h30"/><circle cx="18" cy="10" r="3" fill="#fff"/><circle cx="30" cy="22" r="3" fill="#fff"/><circle cx="14" cy="34" r="3" fill="#fff"/></g></svg>
    <div class="num">STEP 1</div><h4>Explore Your Choices</h4><p>• Pricing<br>• Trial<br>• Quote<br>• Hardware</p>
  </div>
  <div class="step" style="left:476px;top:182px">
    <svg class="step-icon" width="44" height="44" viewBox="0 0 44 44"><g fill="none" stroke="var(--blue)" stroke-width="2.5"><circle cx="22" cy="22" r="13"/><circle cx="22" cy="22" r="5"/><path d="M22 3v6M22 35v6M3 22h6M35 22h6"/></g></svg>
    <div class="num">STEP 2</div><h4>Get Setup</h4><p>• Input Your Alerts<br>• Input Your Staff<br>• Install Our Software</p>
  </div>
  <div class="step" style="left:813px;top:182px">
    <svg class="step-icon" width="44" height="44" viewBox="0 0 44 44"><g fill="none" stroke="var(--blue)" stroke-width="2.5"><path d="M22 3l16 6v11c0 11-8 18-16 21C14 38 6 31 6 20V9z"/><circle cx="22" cy="18" r="4"/><path d="M14 30c2-5 14-5 16 0"/></g></svg>
    <div class="num">STEP 3</div><h4>Feel Confident Your<br>Staff is Protected</h4><p>High Five. You just too<br>a major step to getting rid of<br>the anxiety and frustration<br>this gave you.</p>
  </div>
  <div class="btn blue" style="left:491px;top:532px;width:218px;height:35px">Start my demo</div>
</section>

<section class="connected">
  <div class="mockup" style="left:83px;top:74px;width:677px;height:413px" role="img" aria-label="Laptop showing an emergency alert conversation, with a lanyard panic button in front"></div>
  <svg class="abs" style="left:660px;top:162px" width="72" height="34" viewBox="0 0 72 34"><path d="M70 26C50 8 26 6 6 16" fill="none" stroke="var(--green)" stroke-width="2.5"/><path d="M16 6L4 17l14 6" fill="none" stroke="var(--green)" stroke-width="2.5"/></svg>
  <h2 class="abs connected-title"><span class="hl">Stay connected</span> with staff<br>during a crisis situation</h2>
  <div class="btn blue" style="left:750px;top:229px;width:218px;height:34px">Start my demo</div>
</section>

<footer class="footer">
  <div class="brand" style="left:83px;top:104px;font-size:26px"><span class="dot" style="width:40px;height:40px"></span>CrewBeacon</div>
  <p class="abs foot-about">When employees feel alone during a threatening situation, we give them a way to let the right resources know that they need help so you can feel confident that your staff is protected.</p>
  <div class="foot-col" style="left:352px"><h5>SHOP</h5><ul><li>Add Ons</li><li>Start My Demo</li><li>Custom Quote</li><li>Start Trial</li></ul></div>
  <div class="foot-col" style="left:512px"><h5>ABOUT</h5><ul><li>Affiliates</li><li>Contact</li><li>Support</li><li>Existing Customers</li><li>Industries</li><li>Blog</li><li>FAQ</li></ul></div>
  <div class="foot-col" style="left:691px"><h5>LEGAL</h5><ul><li>Privacy Policy</li><li>Terms of Use</li><li>End User License Agreement</li></ul></div>
  <div class="call">
    <svg width="26" height="26" viewBox="0 0 24 24"><path d="M6.6 10.8a15 15 0 0 0 6.6 6.6l2.2-2.2c.3-.3.7-.4 1-.2 1.1.4 2.3.6 3.6.6.6 0 1 .4 1 1V20c0 .6-.4 1-1 1A17 17 0 0 1 3 4c0-.6.4-1 1-1h3.5c.6 0 1 .4 1 1 0 1.3.2 2.5.6 3.6.1.3 0 .7-.2 1z" fill="#fff"/></svg>
    <div><b>Call Us</b><strong>1-800-555-0142</strong></div>
  </div>
  <div class="social"><span></span><span></span><span></span><span></span></div>
  <div class="abs legal-links">PRIVACY POLICY &nbsp; | &nbsp; COOKIE POLICY &nbsp; | &nbsp; DATA USAGE POLICY<br>© 2020 CREWBEACON - ALL RIGHTS RESERVED</div>
</footer>

<section class="newsletter">
  <h2>Subscribe for our <span class="hl-green">newsletter</span></h2>
  <div class="field">Enter Email Address</div>
  <div class="btn blue">Subscribe</div>
</section>

</body>
</html>
```